Bref créative
vostelmira #20
Real Estate Investors
Professional
Dale Quistorff
President
8316 Willowmere Rd, Ste. 217 (#492)
Harlow Bend, TX 75990
dquistorff@mailvessa.com
Please make 100 cards in the name of Dale Quistorff and the other 100 cards in the name of: Colette Quistorff, Title: Program Director, Address: Same, Phone: Same, Cell: 214 637-2940, E-mail: colette.quistorff@mailvessa.com.
Keep in mind we will request an update on this card in a later date with the following: Website Address, Fax #, and Toll Free #.

```html
<!DOCTYPE html>
<html lang="en">
<head>
<meta charset="utf-8">
<title>Tolvanex Stationery Set</title>
<link rel="stylesheet" href="https://fonts.googleapis.com/css2?family=Cinzel:wght@600&family=Open+Sans:wght@400;600&display=swap">
<style>
:root{
  --bg:#e6e3de;
  --paper:#ffffff;
  --ink:#3a3a3a;
  --muted:#7d7d7d;
  --red:#c8202a;
  --black:#121212;
  --charcoal:#2a2a2a;
  --silver:#b9b9b9;
  --light:#cfcfcf;
}
*{box-sizing:border-box;margin:0;padding:0}
html,body{width:1200px;height:670px;overflow:hidden}
body{background:var(--bg);font-family:"Open Sans",Arial,sans-serif;color:var(--ink);position:relative}
.piece{position:absolute;background:var(--paper);box-shadow:0 2px 8px rgba(0,0,0,.18);overflow:hidden}
.brand{display:flex;align-items:center;gap:6px;font-family:"Cinzel",Georgia,serif;font-weight:600;color:var(--red);letter-spacing:.06em;white-space:nowrap}
.brand-mark{width:9px;height:9px;background:var(--red);flex:none}
.small{font-size:7px;line-height:1.45;color:var(--muted);white-space:nowrap}
.stripe{position:absolute;display:flex;gap:3px;align-items:stretch;height:6px}
.stripe span{display:block;width:10px;background:var(--red)}
.stripe span.grey{background:var(--silver);width:4px}
.rule{position:absolute;height:1px;background:var(--silver)}

/* letterhead */
.letterhead{left:40px;top:40px;width:440px;height:590px}
.letterhead .brand{position:absolute;left:36px;top:36px;font-size:22px}
.letterhead .address{position:absolute;right:36px;top:36px;text-align:right}
.letterhead .rule{left:36px;right:36px;top:82px}
.letterhead .rule.bottom{top:auto;bottom:40px}
.letterhead .stripe{left:36px;bottom:26px}

/* envelope front */
.envelope{left:520px;top:40px;width:320px;height:170px}
.envelope .brand{position:absolute;left:20px;top:20px;font-size:15px}
.envelope .address{position:absolute;left:20px;top:44px}
.envelope .stripe{right:20px;bottom:16px}
.envelope .rule{left:20px;right:20px;bottom:28px}

/* envelope back */
.envelope-back{left:520px;top:250px;width:320px;height:170px}
.envelope-back svg{position:absolute;left:0;top:0}
.envelope-back .brand{position:absolute;left:0;right:0;top:22px;justify-content:center;font-size:14px;color:var(--paper)}

/* compliment card */
.compliment{left:520px;top:460px;width:320px;height:170px}
.compliment .brand{position:absolute;left:20px;top:20px;font-size:15px}
.compliment .address{position:absolute;left:20px;top:44px}
.compliment .stripe{right:20px;bottom:16px}
.compliment .rule{left:20px;right:20px;bottom:28px}

/* business cards */
.card{width:280px;height:160px;background:linear-gradient(135deg,var(--charcoal) 0%,var(--black) 60%)}
.card-front{left:880px;top:40px}
.card-back{left:880px;top:245px}
.card-back.second{top:450px}
.card-front .brand{position:absolute;left:0;right:0;top:66px;justify-content:center;font-size:20px;color:var(--paper)}
.card .band{position:absolute;left:0;right:0;bottom:22px;height:4px;background:var(--silver);opacity:.5}
.card .stripe{left:18px;bottom:20px;height:8px}
.card-back .brand{position:absolute;left:18px;top:16px;font-size:12px;color:var(--paper)}
.person{position:absolute;left:18px;top:44px;right:18px}
.person .name{font-family:"Cinzel",Georgia,serif;font-weight:600;font-size:12px;color:var(--paper);letter-spacing:.04em}
.person .title{font-size:8px;color:var(--red);font-weight:600;text-transform:uppercase;letter-spacing:.08em;margin-top:2px}
.person .details{font-size:7.5px;line-height:1.5;color:var(--light);margin-top:8px;white-space:nowrap}
</style>
</head>
<body>

<section class="piece letterhead">
  <div class="brand"><span class="brand-mark"></span>Tolvanex</div>
  <div class="address small">
    8316 Willowmere Rd, Ste. 217 (#492)<br>
    Harlow Bend, TX 75990<br>
    dquistorff@mailvessa.com
  </div>
  <div class="rule"></div>
  <div class="rule bottom"></div>
  <div class="stripe"><span></span><span class="grey"></span><span></span><span class="grey"></span></div>
</section>

<section class="piece envelope">
  <div class="brand"><span class="brand-mark"></span>Tolvanex</div>
  <div class="address small">
    8316 Willowmere Rd, Ste. 217 (#492)<br>
    Harlow Bend, TX 75990
  </div>
  <div class="rule"></div>
  <div class="stripe"><span></span><span class="grey"></span><span></span><span class="grey"></span></div>
</section>

<section class="piece envelope-back">
  <svg width="320" height="170" viewBox="0 0 320 170" aria-hidden="true">
    <path d="M0 0 H320 V52 Q160 100 0 52 Z" fill="#121212"/>
  </svg>
  <div class="brand"><span class="brand-mark"></span>Tolvanex</div>
</section>

<section class="piece compliment">
  <div class="brand"><span class="brand-mark"></span>Tolvanex</div>
  <div class="address small">
    8316 Willowmere Rd, Ste. 217 (#492)<br>
    Harlow Bend, TX 75990
  </div>
  <div class="rule"></div>
  <div class="stripe"><span></span><span class="grey"></span><span></span><span class="grey"></span></div>
</section>

<section class="piece card card-front">
  <div class="brand"><span class="brand-mark"></span>Tolvanex</div>
  <div class="band"></div>
  <div class="stripe"><span></span><span class="grey"></span><span></span></div>
</section>

<section class="piece card card-back">
  <div class="brand"><span class="brand-mark"></span>Tolvanex</div>
  <div class="person">
    <div class="name">Dale Quistorff</div>
    <div class="title">President</div>
    <div class="details">
      8316 Willowmere Rd, Ste. 217 (#492)<br>
      Harlow Bend, TX 75990<br>
      dquistorff@mailvessa.com
    </div>
  </div>
  <div class="band"></div>
  <div class="stripe"><span></span><span class="grey"></span><span></span></div>
</section>

<section class="piece card card-back second">
  <div class="brand"><span class="brand-mark"></span>Tolvanex</div>
  <div class="person">
    <div class="name">Colette Quistorff</div>
    <div class="title">Program Director</div>
    <div class="details">
      8316 Willowmere Rd, Ste. 217 (#492)<br>
      Harlow Bend, TX 75990 &middot; Cell: 555 017-2940<br>
      colette.quistorff@mailvessa.com
    </div>
  </div>
  <div class="band"></div>
  <div class="stripe"><span></span><span class="grey"></span><span></span></div>
</section>

</body>
</html>
```